Graphic Design For Website Banner + 4 Product Images - More Work To Follow

We are in the process of launching a new website. I need to design a banner for the homepage, as well as some graphics for my product images.

Please find attached -

1) My current logo.
2) Banner Sample + Product Image Sample - both of these are a screenshot from a common website that I like the design and style of.
3) Colour Scheme Sample 1 - saved image showing colour scheme for BrushOtter that I like.
4) Colour Scheme Sample 2 - Saved image showing colour scheme for Plivo that I like.
5) Sample 1-4 - These are colour palette samples I created online showing what I like.
6) 4 blank product images to show what is required in the design.

To summarise I'll like to create a banner design and product images similar to what's been attached and have a consistent colour theme throughout. I'm happy to adjust the colours in my logo to match the final designs.

To begin with I'll be requesting 1 banner design and 4 product images. I'll have more work for the successful designer.

Banner -
Size to be 950x300. To contain the following wording -
Quality Printing
Offset|Digital|Wideformat
Deal Direct & Save
Possibly include some product images like the sample banner attached.

Product Images -
Size to be 263x263
1) Business Cards
2) Folded Brochures
3) Flyers
4) Presentation Folders
I've attached blank sample images of all 4 for your reference.

Please feel free to ask any questions as I'm happy to give further direction.

Target Market(s)

We are a commercial Printer offering a range of printed products

Font styles to use
Serif
Sans Serif

Colors
34a6d7
33b8a4
3277b5
86cfc7
86cae7
85acd3
00a990
0393ce
0255a3

```html
<!DOCTYPE html>
<html lang="en">
<head>
<meta charset="utf-8">
<title>Business Cards – Product Image</title>
<link rel="stylesheet" href="https://fonts.googleapis.com/css2?family=Open+Sans:wght@400;600&display=swap">
<style>
  :root {
    --bg-teal: #4a9fae;
    --bg-mint: #93cabe;
    --bg-sky: #8fc3de;
    --bg-blue: #3b97d6;
    --card-back: #f1f1f3;
    --card-front: #ebebed;
    --card-edge: #d9dadd;
  }
  html, body {
    margin: 0;
    padding: 0;
    width: 1200px;
    height: 1200px;
    overflow: hidden;
    font-family: "Open Sans", sans-serif;
  }
  .product-tile {
    position: relative;
    width: 1200px;
    height: 1200px;
    background: linear-gradient(135deg,
      var(--bg-teal) 0%,
      var(--bg-teal) 12%,
      var(--bg-mint) 40%,
      var(--bg-sky) 66%,
      var(--bg-blue) 100%);
  }
  .card-stack {
    position: absolute;
    inset: 0;
    width: 1200px;
    height: 1200px;
  }
</style>
</head>
<body>
  <main class="product-tile">
    <svg class="card-stack" viewBox="0 0 1200 1200" role="img" aria-label="Two blank white business cards, one laid over the other at an angle">
      <polygon class="card card-back" points="342,319 766,411 725,661 269,588" fill="var(--card-back)"/>
      <polygon class="card card-front" points="449,611 887,538 931,814 493,885" fill="var(--card-front)" stroke="var(--card-edge)" stroke-width="1"/>
    </svg>
  </main>
</body>
</html>
```